Labels for fruit liqueur bottles

We are looking for a visual identity based on our logo, for fruit liqueur labels. To date, we have different liqueurs such as: lemon liqueur, orange liqueurs, mandarin liqueurs, grapefruit liqueurs. We will then create other liqueurs such as strawberry, apple or even apricot. Our goal is to have a single visual that we can adapt in different colors depending on the fruit used.

On the label there should be:
the logo
homemade
the name of the fruit (which can be changed depending on the product)
swiss-made
50cl
21°

Colors

Designer to choose colors to be used in the design.

Requirements
Must have
• a visual of liquor bottle labels, with the possibility of changing the background colors, depending on the fruit used
Nice to have
• something modern and nice to look at. We must be able to read the basic fruit in the blink of an eye. it is also possible to have a black or white or colored label background.

```html
<!DOCTYPE html>
<html lang="en">
<head>
<meta charset="utf-8">
<title>Casa Veldini – Fruit Liqueur Labels</title>
<link rel="stylesheet" href="https://fonts.googleapis.com/css2?family=Oswald:wght@600&family=Poppins:wght@500;600&family=Lobster&display=swap">
<style>
  :root {
    --canvas: #f6ead3;
    --brand-orange: #f05a23;
    --white: #ffffff;
    --swiss-red: #e3262b;

    --lemon-top: #083a21;
    --lemon-field: #8cc63f;
    --lemon-ink: #0b3d21;
    --lemon-small: #1d5b26;

    --grape-top: #4a1454;
    --grape-field: #c043b8;
    --grape-ink: #4b1a5c;
    --grape-small: #f6cdf0;

    --orange-top: #1c2d6b;
    --orange-field: #f15a22;
    --orange-ink: #1c2d6b;
    --orange-small: #ffe3a6;
  }
  * { box-sizing: border-box; margin: 0; padding: 0; }
  html, body { width: 1000px; height: 1200px; overflow: hidden; }
  body {
    background: var(--canvas);
    display: flex;
    align-items: center;
    justify-content: center;
  }
  .label-row {
    display: flex;
    gap: 20px;
  }
  .label {
    position: relative;
    width: 310px;
    height: 362px;
    background: var(--top);
    overflow: hidden;
    text-align: center;
  }
  .label--lemon  { --top: var(--lemon-top);  --field: var(--lemon-field);  --ink: var(--lemon-ink);  --small: var(--lemon-small); --fruit-a: #f7e01c; --fruit-b: #fff6a0; }
  .label--grape  { --top: var(--grape-top);  --field: var(--grape-field);  --ink: var(--grape-ink);  --small: var(--grape-small); --fruit-a: #3b1f6b; --fruit-b: #5a3a90; }
  .label--orange { --top: var(--orange-top); --field: var(--orange-field); --ink: var(--orange-ink); --small: var(--orange-small); --fruit-a: #f7931e; --fruit-b: #ffc27a; }

  .label__field {
    position: absolute;
    inset: 0;
    width: 310px;
    height: 362px;
  }
  .label__field .wave { fill: var(--field); }
  .label__field .fruit-glow { fill: url(#none); }

  .brand {
    position: absolute;
    top: 16px;
    left: 0;
    right: 0;
  }
  .brand__dot {
    display: block;
    width: 48px;
    height: 48px;
    margin: 0 auto 12px;
    border-radius: 50%;
    background: var(--brand-orange);
  }
  .brand__name {
    font-family: "Poppins", sans-serif;
    font-weight: 600;
    font-size: 21px;
    line-height: 1;
    letter-spacing: -0.2px;
    color: var(--brand-orange);
  }
  .brand__tagline {
    margin-top: 3px;
    font-family: "Poppins", sans-serif;
    font-weight: 500;
    font-size: 11px;
    letter-spacing: 0.6px;
    color: var(--brand-orange);
  }

  .product {
    position: absolute;
    top: 188px;
    left: 0;
    right: 0;
  }
  .product__homemade {
    font-family: "Lobster", cursive;
    font-size: 18px;
    line-height: 1;
    color: var(--ink);
  }
  .product__name {
    margin-top: 6px;
    font-family: "Oswald", sans-serif;
    font-weight: 600;
    font-size: 46px;
    line-height: 0.98;
    letter-spacing: -0.5px;
    text-transform: uppercase;
    color: var(--ink);
  }
  .product__volume {
    position: absolute;
    left: 0;
    right: 0;
    bottom: 14px;
    font-family: "Poppins", sans-serif;
    font-weight: 500;
    font-size: 11px;
    letter-spacing: 0.3px;
    color: var(--small);
  }

  .swiss-badge {
    position: absolute;
    right: 18px;
    bottom: 20px;
    width: 18px;
    height: 46px;
    background: var(--white);
  }
  .swiss-badge::after {
    content: "";
    position: absolute;
    left: 2px;
    right: 2px;
    bottom: 2px;
    height: 14px;
    background: var(--swiss-red);
  }
</style>
</head>
<body>
  <main class="label-row">

    <article class="label label--lemon">
      <svg class="label__field" viewBox="0 0 310 362" role="img" aria-label="Lemon halves, lemon slices and green leaves scattered across a lime green field">
        <defs>
          <radialGradient id="lemon-glow" cx="50%" cy="70%" r="70%">
            <stop offset="0" stop-color="#9fd24f"/>
            <stop offset="1" stop-color="#8cc63f"/>
          </radialGradient>
        </defs>
        <path class="wave" fill="url(#lemon-glow)" d="M0 158 C40 142 80 150 120 158 S200 164 240 150 S290 128 310 136 V362 H0 Z"/>
      </svg>
      <header class="brand">
        <span class="brand__dot"></span>
        <p class="brand__name">CASA VELDINI</p>
        <p class="brand__tagline">liqueur de fruits</p>
      </header>
      <section class="product">
        <p class="product__homemade">Home Made</p>
        <h2 class="product__name">Lemon<br>Liqueur</h2>
      </section>
      <p class="product__volume">50CL - 21% VOL</p>
      <span class="swiss-badge" aria-hidden="true"></span>
    </article>

    <article class="label label--grape">
      <svg class="label__field" viewBox="0 0 310 362" role="img" aria-label="Dark purple grape berries with green leaves scattered across a magenta field">
        <defs>
          <radialGradient id="grape-glow" cx="50%" cy="70%" r="70%">
            <stop offset="0" stop-color="#c94cc0"/>
            <stop offset="1" stop-color="#b53aae"/>
          </radialGradient>
        </defs>
        <path class="wave" fill="url(#grape-glow)" d="M0 158 C40 142 80 150 120 158 S200 164 240 150 S290 128 310 136 V362 H0 Z"/>
      </svg>
      <header class="brand">
        <span class="brand__dot"></span>
        <p class="brand__name">CASA VELDINI</p>
        <p class="brand__tagline">liqueur de fruits</p>
      </header>
      <section class="product">
        <p class="product__homemade">Home Made</p>
        <h2 class="product__name">Grape<br>Liqueur</h2>
      </section>
      <p class="product__volume">50CL - 21% VOL</p>
      <span class="swiss-badge" aria-hidden="true"></span>
    </article>

    <article class="label label--orange">
      <svg class="label__field" viewBox="0 0 310 362" role="img" aria-label="Orange halves, orange slices and green leaves scattered across a bright orange field">
        <defs>
          <radialGradient id="orange-glow" cx="50%" cy="70%" r="70%">
            <stop offset="0" stop-color="#f4702c"/>
            <stop offset="1" stop-color="#f15a22"/>
          </radialGradient>
        </defs>
        <path class="wave" fill="url(#orange-glow)" d="M0 158 C40 142 80 150 120 158 S200 164 240 150 S290 128 310 136 V362 H0 Z"/>
      </svg>
      <header class="brand">
        <span class="brand__dot"></span>
        <p class="brand__name">CASA VELDINI</p>
        <p class="brand__tagline">liqueur de fruits</p>
      </header>
      <section class="product">
        <p class="product__homemade">Home Made</p>
        <h2 class="product__name">Orange<br>Liqueur</h2>
      </section>
      <p class="product__volume">50CL - 21% VOL</p>
      <span class="swiss-badge" aria-hidden="true"></span>
    </article>

  </main>
</body>
</html>
```